Infoblatt
Zielgruppe
Talentförderung, Personalentwicklung, Beratung von Personalabteilungen
Zielgruppe: Personaler, HR Verantwortliche
Aufgabenstellung
Es geht um einen "One-Pager", der auf einem Kongress ausgelegt werden soll und in Kurzform einen Überblick über unser Unternehmen und unser Angebot informieren soll.
Wir haben Visitenkarten auf Recyclingpapier und möchten das Blatt konsistent auf das gleiche Papier drucken lassen, daher einfarbig schwarz. Format DIN A4 Hoch.
IDEE: Vom Stil wie eine Infografik aufbauen
TYPO: unser LOGO ist BEBAS NEUE und unsere Schrift Helvetica

```html
<!DOCTYPE html>
<html lang="de">
<head>
<meta charset="utf-8">
<title>Kernwerk – Infoblatt</title>
<link href="https://fonts.googleapis.com/css2?family=Source+Sans+3:wght@400;700&family=Herr+Von+Muellerhoff&display=swap" rel="stylesheet">
<style>
  :root {
    --stage: #ececec;
    --ink: #1c1c1c;
    --panel-dark: #333333;
    --panel-light: rgba(226, 226, 226, 0.88);
    --text-dark: #2a2a2a;
    --text-light: #f2f2f2;
    --paper: #ffffff;
  }
  * { box-sizing: border-box; margin: 0; padding: 0; }
  html, body { width: 1200px; height: 850px; overflow: hidden; background: var(--stage); }
  body { position: relative; font-family: "Source Sans 3", "Helvetica Neue", Arial, sans-serif; }

  .sheet {
    position: absolute; left: 330px; top: 45px; width: 536px; height: 757px;
    background: var(--paper); overflow: hidden;
    box-shadow: 0 1px 4px rgba(0, 0, 0, 0.12);
  }
  .tile { position: absolute; }

  .brand-bar { left: 0; top: 0; width: 268px; height: 92px; background: var(--ink); }
  .brand-name {
    position: absolute; left: 26px; top: 26px;
    font-weight: 700; font-size: 38px; letter-spacing: 0.5px; line-height: 1;
    color: var(--paper); text-transform: uppercase;
  }

  .belief { left: 0; top: 92px; width: 268px; height: 161px;
    background: linear-gradient(90deg, #ededed, #dcdcdc 60%, #cfcfcf); }
  .photo-dartboard { left: 268px; top: 0; width: 268px; height: 253px;
    background: radial-gradient(circle at 50% 58%, #d8d8d8 0 10%, #4a4a4a 30%, #9a9a9a 55%, #5c5c5c 80%, #cfcfcf 100%); }
  .photo-meeting { left: 0; top: 253px; width: 268px; height: 253px;
    background: linear-gradient(110deg, #5a5a5a 0%, #d0d0d0 30%, #eeeeee 50%, #3d3d3d 75%, #1e1e1e 100%); }
  .offer { left: 268px; top: 253px; width: 268px; height: 253px; background: var(--panel-dark); }
  .photo-workshop { left: 0; top: 506px; width: 536px; height: 251px;
    background: linear-gradient(180deg, #4a4a4a 0%, #2e2e2e 45%, #9b9b9b 75%, #595959 100%); }
  .principles { left: 0; top: 506px; width: 268px; height: 251px; background: var(--panel-light); }

  .script-head {
    font-family: "Herr Von Muellerhoff", cursive;
    font-size: 42px; line-height: 34px; font-weight: 400; white-space: nowrap;
  }
  .copy { font-size: 9.5px; line-height: 13.5px; }
  .copy p + p { margin-top: 5px; }
  .copy strong { font-weight: 700; }

  .belief .script-head { position: absolute; left: 25px; top: 24px; color: var(--ink); }
  .belief .copy { position: absolute; left: 25px; top: 64px; width: 205px; color: var(--text-dark); }

  .offer .script-head { position: absolute; left: 25px; top: 25px; color: var(--text-light); }
  .offer .copy { position: absolute; left: 25px; top: 61px; width: 218px; color: var(--text-light); }
  .offer .copy .group-title { font-weight: 700; text-transform: uppercase; margin-top: 10px; }
  .service-list { list-style: none; }
  .service-list li::before { content: "•"; margin-right: 5px; }

  .principles .script-head { position: absolute; left: 25px; top: 14px; color: var(--ink); line-height: 25px; }
  .principles .underline { position: absolute; left: 25px; top: 74px; }
  .principles .copy { position: absolute; left: 25px; top: 89px; width: 245px; color: var(--text-dark); }
</style>
</head>
<body>
<main class="sheet">
  <div class="tile photo-dartboard" role="img" aria-label="Schwarzweißfoto einer Dartscheibe"></div>

  <header class="tile brand-bar">
    <div class="brand-name">Kernwerk</div>
  </header>

  <section class="tile belief">
    <h2 class="script-head">Woran wir glauben</h2>
    <div class="copy">
      <p>Wir glauben, dass sich persönliche und ökonomische Werte ergänzen - mehr noch, dass sie langfristig nicht ohne einander auskommen und dass sich emotionale Bindung als Mehrwert in Zahlen ausdrückt.</p>
    </div>
  </section>

  <div class="tile photo-meeting" role="img" aria-label="Unscharfes Schwarzweißfoto einer Besprechung mehrerer Personen"></div>

  <section class="tile offer">
    <h2 class="script-head">Was wir bieten</h2>
    <div class="copy">
      <p>Wir beraten Unternehmen im Rahmen der Talentförderung und helfen Jugendlichen auf dem Weg in ihr Berufsleben.</p>
      <p class="group-title">Für Unternehmen</p>
      <ul class="service-list">
        <li>Talentförderung &amp; Talent Management</li>
        <li>Professionalisierung der Personalarbeit</li>
        <li>Organisationsentwicklung</li>
        <li>Potentialorientierte Mitarbeiterführung</li>
      </ul>
      <p class="group-title">Für die junge Generation</p>
      <ul class="service-list">
        <li>Berufsorientierung</li>
        <li>Bewerbungscoaching</li>
      </ul>
    </div>
  </section>

  <div class="tile photo-workshop" role="img" aria-label="Schwarzweißfoto eines Arbeitstisches mit Papierrollen und Markern vor einer Holzwand"></div>

  <section class="tile principles">
    <h2 class="script-head">Was unser<br>Handeln leitet</h2>
    <svg class="underline" width="190" height="6" viewBox="0 0 190 6" aria-hidden="true">
      <path d="M60 3 C100 2 150 2 188 3" stroke="#1c1c1c" stroke-width="1" fill="none"/>
    </svg>
    <div class="copy">
      <p>Kundare heißt marktschreierisch anpreisen, hinters Licht führen, täuschen. Mandare heißt beauftragen, Vertrauen schenken. Wir legen großen Wert auf eine Beziehung, die Mandare, nicht Kundare entspricht.</p>
      <p>Für uns ist der partnerschaftliche Umgang mit unseren Mandanten das Fundament.</p>
      <p><strong>Wir haben keine Kunden.<br>Wir unterstützen Mandanten.</strong></p>
    </div>
  </section>
</main>
</body>
</html>
```